Health IT software startup needs a product sheet to promote our software/company

-Need a one page product sheet that highlights our software and company for our customers.
-Our software is an EHR (electronic health record) software for hospitals.
-Attached is our logo (2 options-picture 4,5). Our caption with the logo should read "An EHR developed by physicians and healthcare professionals with decades of experience in behavioral health".
-Incorporate another smaller sub-heading (section) in the product sheet- titled "How Calvento Helps You"- with three associated words- 'Quality, Familiarity, Security'.
-Incorporate the main section titled "Our Software" with a description of the software with 3 components to use- see attached word document- Calvento Product Sheet.
-Attached is a optional photo you may consider if you like- we currently use it on our website with our logo and logo caption- see attached homepage-resized.jpg
-you can additional royalty free photos as needed
-Finally, the 'Contact Us' information:
404-555-0187
info@calventosoftware.example
www.calventosoftware.example

Target Market(s)

Behavioral Health Hospitals- specifically the product sheet will be left with the customers after we demo the software to them.

Font styles to use
Serif
Sans Serif

Colors
0555a3
3276b5
85acd3
0393ce
33a6d7
00a990
cedeed
ecf7fb
33b8a4

Requirements
Should not have
• Please do not saturate the product sheet with only colors- utilize white space

```html
<!DOCTYPE html>
<html lang="en">
<head>
<meta charset="utf-8">
<title>Calvento Product Sheet</title>
<link href="https://fonts.googleapis.com/css2?family=Roboto+Condensed:wght@300;400&family=Lato:wght@300;400&display=swap" rel="stylesheet">
<style>
  :root {
    --navy: #1c2672;
    --navy-deep: #18205f;
    --royal: #0555a3;
    --cyan: #0393ce;
    --sky: #33a6d7;
    --ink: #3a3a3a;
    --stone-light: #9aa1aa;
    --stone-dark: #6a717b;
    --backdrop: #e6eaf0;
    --white: #ffffff;
  }
  * { margin: 0; padding: 0; box-sizing: border-box; }
  html, body { width: 1200px; height: 2400px; overflow: hidden; background: var(--backdrop); }
  .sheet {
    position: absolute; left: 0; top: 353px;
    width: 1200px; height: 1694px;
    background: var(--white); overflow: hidden;
    font-family: "Lato", Arial, sans-serif;
  }
  .brand {
    position: absolute; left: 77px; top: 62px;
    display: flex; align-items: center; gap: 22px;
  }
  .brand-mark { width: 70px; height: 70px; border-radius: 50%; background: var(--navy); }
  .brand-name {
    font-family: "Lato", Arial, sans-serif; font-weight: 300;
    font-size: 74px; color: var(--navy); letter-spacing: 2px; line-height: 1;
  }
  .shapes { position: absolute; left: 0; top: 0; }
  .hero-photo { position: absolute; left: 0; top: 0; }
  .intro { position: absolute; left: 60px; top: 222px; width: 500px; color: var(--white); }
  .headline {
    font-family: "Roboto Condensed", "Arial Narrow", sans-serif; font-weight: 400;
    font-size: 48px; line-height: 1; letter-spacing: 0.3px; white-space: nowrap;
  }
  .subline { font-size: 24px; font-weight: 300; line-height: 31px; margin-top: 8px; white-space: nowrap; }
  .headline.second { margin-top: 10px; }
  .accent-rule { width: 160px; height: 4px; background: var(--sky); margin-top: 16px; }
  .helps-title {
    font-family: "Roboto Condensed", "Arial Narrow", sans-serif; font-weight: 300;
    font-size: 29px; margin-top: 26px; margin-left: 4px;
  }
  .benefits { display: flex; gap: 28px; margin-top: 28px; margin-left: 4px; align-items: center; list-style: none; }
  .benefit { display: flex; align-items: center; gap: 12px; font-size: 19px; }
  .benefit svg { width: 46px; height: 46px; }
  .section-title {
    position: absolute; left: 66px; top: 634px;
    font-family: "Roboto Condensed", "Arial Narrow", sans-serif; font-weight: 300;
    font-size: 42px; color: var(--white);
  }
  .feature {
    position: absolute; width: 420px; text-align: center;
    font-family: "Roboto Condensed", "Arial Narrow", sans-serif; font-weight: 300;
    font-size: 39px; line-height: 48px;
  }
  .feature svg { display: block; margin: 0 auto 20px; }
  .feature .dark { color: var(--navy); display: block; }
  .feature .light { color: var(--cyan); display: block; }
  .feature.documentation { left: 52px; top: 766px; }
  .feature.engagement { left: 52px; top: 1028px; }
  .feature.risk { left: 52px; top: 1284px; }
  .copy {
    position: absolute; left: 500px; width: 578px;
    font-size: 20.5px; line-height: 26.6px; color: var(--ink);
    text-align: justify; hyphens: auto; font-weight: 400;
  }
  .copy.one { top: 782px; }
  .copy.two { top: 1016px; }
  .copy.three { top: 1304px; }
  .call-now {
    position: absolute; left: 47px; top: 1614px;
    font-size: 37px; font-weight: 300; color: var(--white); letter-spacing: 0.3px; white-space: nowrap;
  }
  .contact {
    position: absolute; left: 590px; top: 1630px;
    display: flex; align-items: center; gap: 7px; white-space: nowrap;
    font-size: 16.5px; color: var(--white);
  }
  .contact svg { width: 16px; height: 16px; }
  .contact .gap { width: 4px; }
</style>
</head>
<body>
<main class="sheet">
  <svg class="shapes" width="1200" height="1694" viewBox="0 0 1200 1694">
    <defs>
      <linearGradient id="panelGrad" x1="0" y1="0" x2="0" y2="1">
        <stop offset="0" stop-color="#0555a3"/>
        <stop offset="0.55" stop-color="#123f91"/>
        <stop offset="1" stop-color="#1c2672"/>
      </linearGradient>
      <linearGradient id="footGrad" x1="0" y1="0" x2="1" y2="0">
        <stop offset="0" stop-color="#1c2672"/>
        <stop offset="1" stop-color="#2b3a9e"/>
      </linearGradient>
    </defs>
    <polygon points="0,174 574,174 574,580 660,618 0,618" fill="url(#panelGrad)"/>
    <polygon points="0,618 540,618 481,711 0,711" fill="var(--cyan)"/>
    <polygon points="0,1590 570,1590 503,1694 0,1694" fill="var(--cyan)"/>
    <polygon points="582,1590 1200,1590 1200,1694 515,1694" fill="url(#footGrad)"/>
  </svg>

  <svg class="hero-photo" width="1200" height="760" viewBox="0 0 1200 760" role="img" aria-label="Photo: a diverse team of professionals seen from above, joining hands in a circle on a stone plaza">
    <defs>
      <linearGradient id="stoneGrad" x1="0" y1="0" x2="1" y2="1">
        <stop offset="0" stop-color="#9aa1aa"/>
        <stop offset="0.5" stop-color="#7b828c"/>
        <stop offset="1" stop-color="#666d77"/>
      </linearGradient>
    </defs>
    <polygon points="581,213 739,0 1200,0 1200,589 908,755 581,574" fill="url(#stoneGrad)"/>
  </svg>

  <div class="brand">
    <span class="brand-mark"></span>
    <span class="brand-name">Calvento</span>
  </div>

  <section class="intro">
    <h1 class="headline">AN EHR DEVELOPED BY</h1>
    <p class="subline">Physicians and Healthcare professionals<br>with decades of experience in</p>
    <h1 class="headline second">BEHAVIORAL HEALTH</h1>
    <div class="accent-rule"></div>
    <h2 class="helps-title">HOW CALVENTO HELPS YOU</h2>
    <ul class="benefits">
      <li class="benefit">
        <svg viewBox="0 0 46 46"><circle cx="23" cy="23" r="23" fill="#0393ce"/><circle cx="23" cy="20" r="7" fill="none" stroke="#fff" stroke-width="1.8"/><path d="M18 26 L15 34 L19 32 L21 35 L23 27 M28 26 L31 34 L27 32 L25 35 L23 27" fill="none" stroke="#fff" stroke-width="1.6"/></svg>
        Quality
      </li>
      <li class="benefit">
        <svg viewBox="0 0 46 46"><circle cx="23" cy="23" r="23" fill="#0393ce"/><rect x="12" y="13" width="22" height="15" rx="1.5" fill="none" stroke="#fff" stroke-width="1.8"/><path d="M19 33 H27 M23 28 V33 M16 18 H24 M16 22 H28" stroke="#fff" stroke-width="1.6"/></svg>
        Familiarity
      </li>
      <li class="benefit">
        <svg viewBox="0 0 46 46"><circle cx="23" cy="23" r="23" fill="#0393ce"/><rect x="14" y="21" width="18" height="13" rx="2" fill="none" stroke="#fff" stroke-width="1.8"/><path d="M17.5 21 V17 a5.5 5.5 0 0 1 11 0 V21" fill="none" stroke="#fff" stroke-width="1.8"/><path d="M19 27 l3 3 l5 -5" fill="none" stroke="#fff" stroke-width="1.6"/></svg>
        Security
      </li>
    </ul>
  </section>

  <h2 class="section-title">OUR PRODUCT:</h2>

  <div class="feature documentation">
    <svg width="92" height="94" viewBox="0 0 92 94" fill="none" stroke="#0393ce" stroke-width="5">
      <path d="M6 68 V4 H50"/>
      <path d="M16 78 V14 H60"/>
      <path d="M26 90 V24 H66 L84 42 V90 Z"/>
      <path d="M66 24 V42 H84"/>
    </svg>
    <span class="dark">ORGANIC</span>
    <span class="light">DOCUMENTATION</span>
  </div>

  <div class="feature engagement">
    <svg width="96" height="104" viewBox="0 0 96 104" fill="none" stroke="#0393ce" stroke-width="5" stroke-linecap="round" stroke-linejoin="round">
      <circle cx="50" cy="9" r="7" fill="#0393ce" stroke="none"/>
      <path d="M48 22 V46 H66 L72 62"/>
      <path d="M48 32 H62"/>
      <path d="M38 36 a17 17 0 1 0 26 18"/>
      <path d="M6 60 L14 84 Q24 96 40 98 H48"/>
      <path d="M90 60 L82 84 Q72 96 56 98 H48"/>
    </svg>
    <span class="dark">PATIENT</span>
    <span class="light">ENGAGEMENT</span>
  </div>

  <div class="feature risk">
    <svg width="120" height="120" viewBox="0 0 120 120" fill="none" stroke="#0393ce" stroke-width="5" stroke-linejoin="round">
      <path d="M60 4 V12"/>
      <path d="M8 58 Q12 14 60 12 Q108 14 112 58 Q99 48 86 58 Q73 48 60 58 Q47 48 34 58 Q21 48 8 58 Z"/>
      <path d="M60 12 Q44 30 34 58 M60 12 Q76 30 86 58 M60 12 V58"/>
      <circle cx="40" cy="76" r="8"/>
      <circle cx="80" cy="76" r="8"/>
      <path d="M24 116 V98 Q24 88 40 88 Q56 88 56 98 V116 Z"/>
      <path d="M64 116 V98 Q64 88 80 88 Q96 88 96 98 V116 Z"/>
      <path d="M40 92 V108 M80 92 V108" stroke-width="3"/>
    </svg>
    <span class="dark">RISK MANAGEMENT/</span>
    <span class="light">QUALITY IMPROVEMENT</span>
  </div>

  <p class="copy one">Calvento set out to provide behavioral health clinicians a familiar platform to engage in chart level documentation for their patient care. Our software is built using each company’s individualized workflow to provide efficient and valid information. By engaging in that recognized foundation, Calvento achieves the feel of an actual chart with the functionality of an electronic record.</p>

  <p class="copy two">Using our proprietary Calvento Modules, we seamlessly digitalize therapy for use in both individual and group therapy. An optional function of the software, Calvento Modules allow the clinician to individualize therapy in a hospital setting. Furthermore, we incorporate a Family Portal through the software so that therapy can involve the entire family during the client’s hospitalization. This allows the client’s support system to become an integral part of the client’s improvement in the hospital.</p>

  <p class="copy three">To facilitate and navigate the ever-changing regulatory environment, Calvento built tailored risk management/quality improvement capabilities into the software. It is capable of tracking deficiencies in the documentation within the hospital, observing trends in real time to engage risk improvement measures, and providing data required for Quality Measures. Calvento feels this risk functionality will help identify potential errors and issues before they become systemic.</p>

  <p class="call-now">CALL NOW 404-555-0187</p>

  <p class="contact">
    <svg viewBox="0 0 18 18" fill="none" stroke="#33a6d7" stroke-width="1.5"><rect x="2" y="4" width="14" height="10"/><path d="M2 4 L9 10 L16 4"/></svg>
    info@calventosoftware.example
    <span class="gap"></span>
    <svg viewBox="0 0 18 18" fill="none" stroke="#33a6d7" stroke-width="1.5"><circle cx="9" cy="9" r="7"/><ellipse cx="9" cy="9" rx="3" ry="7"/><path d="M2 9 H16"/></svg>
    www.calventosoftware.example
  </p>
</main>
</body>
</html>
```